Visitenkartenvorlage ändern
Zielgruppe
Eventmanagement
Aufgabenstellung
Die beiliegende Visitenkarte wäre das "perfekte" Logo für mich. Da es sich hierbei aber um eine Vorlage eines Online-Druck-Anbieters handelt, darf es leider nur für deren Drucke verwendet werden und nicht für Printwerbung, Homepage etc. Daher sollte es genügend verfremdet werden, so dass ich es verwenden kann.

```html
<!DOCTYPE html>
<html lang="de">
<head>
<meta charset="utf-8">
<title>Neatly Planned – Visitenkarte</title>
<link href="https://fonts.googleapis.com/css2?family=Libre+Baskerville&family=Pinyon+Script&family=Open+Sans&display=swap" rel="stylesheet">
<style>
  :root {
    --backdrop: #e6e2df;
    --card-front: #e4e4e4;
    --card-pattern: #dcdcdc;
    --card-back: #ececeb;
    --ink: #555555;
    --ornament: #6a6a6a;
    --shadow: rgba(0, 0, 0, 0.18);
  }
  * { margin: 0; padding: 0; box-sizing: border-box; }
  html, body {
    width: 1200px;
    height: 603px;
    overflow: hidden;
    background: var(--backdrop);
  }
  .canvas {
    position: relative;
    width: 1200px;
    height: 603px;
  }
  .card {
    position: absolute;
    top: 189px;
    height: 224px;
    box-shadow: 0 6px 14px var(--shadow);
    color: var(--ink);
    font-family: "Libre Baskerville", Georgia, serif;
    text-align: center;
    overflow: hidden;
  }
  .card--front {
    left: 125px;
    width: 376px;
    background: var(--card-front);
  }
  .card--back {
    left: 660px;
    width: 393px;
    background: var(--card-back);
  }
  .pattern-field {
    position: absolute;
    left: 0;
    right: 0;
    top: 66px;
    bottom: 0;
    background: var(--card-pattern);
  }
  .border-ornament {
    position: absolute;
    left: 6px;
    right: 6px;
    top: 58px;
    height: 6px;
    background: var(--ornament);
    opacity: 0.45;
  }
  .crest {
    position: absolute;
    background: var(--ornament);
    border-radius: 40% 40% 45% 45%;
  }
  .card--front .crest { left: 160px; top: 8px; width: 56px; height: 66px; }
  .card--back .crest { left: 157px; top: 82px; width: 80px; height: 82px; }
  .brand-name {
    position: absolute;
    left: 0;
    right: 0;
    font-size: 19px;
    letter-spacing: 0.5px;
  }
  .card--front .brand-name { top: 81px; }
  .card--back .brand-name { top: 46px; font-size: 20px; }
  .tagline {
    position: absolute;
    left: 0;
    right: 0;
    letter-spacing: 0.5px;
  }
  .card--front .tagline { top: 110px; font-size: 9.5px; }
  .card--back .tagline { top: 175px; font-size: 14px; }
  .person-name {
    position: absolute;
    left: 0;
    right: 0;
    top: 138px;
    font-family: "Pinyon Script", cursive;
    font-size: 26px;
  }
  .contact {
    position: absolute;
    bottom: 8px;
    font-family: "Open Sans", Arial, sans-serif;
    font-size: 11px;
    letter-spacing: 0.4px;
  }
  .contact--email { left: 14px; }
  .contact--phone { right: 17px; }
  .website {
    position: absolute;
    left: 0;
    right: 0;
    top: 195px;
    font-size: 11.5px;
  }
</style>
</head>
<body>
<main class="canvas">
  <section class="card card--front">
    <div class="pattern-field" role="img" aria-label="Dezentes florales Damastmuster als Hintergrund"></div>
    <div class="border-ornament" role="img" aria-label="Ornamentale Zierleiste"></div>
    <div class="crest" role="img" aria-label="Ornamentales Wappen mit Blattranken"></div>
    <h1 class="brand-name">NEATLY PLANNED</h1>
    <p class="tagline">EVENTS UND MEHR</p>
    <p class="person-name">Beluntora Venaris</p>
    <p class="contact contact--email">INFO@NEATLY-PLANNED.DE</p>
    <p class="contact contact--phone">+ 49 170 5550192</p>
  </section>

  <section class="card card--back">
    <h2 class="brand-name">NEATLY PLANNED</h2>
    <div class="crest" role="img" aria-label="Ornamentales Wappen mit Blattranken"></div>
    <p class="tagline">EVENTS UND MEHR</p>
    <p class="website">www.neatly-planned.de</p>
  </section>
</main>
</body>
</html>
```